Re-brand our business and design!

We need a simple informational website (editable for in the future use)
We need our logo(we have included logo), name, who we are, and what we do displayed.

This is our current site (which is not acceptable, and only a template site): all our information is on this site, please use it forreferanceofinformation.
Www.brightlanefixers.com

Target Market(s)

Real estate brokers, and realtors,homeowners, and anyone looking for home repairs.

Industry/Entity Type

Business

Number of Pages Required

4 page

Font styles to use
Sans Serif

Requirements
Must have
• Our name, contact info, services, and our logo (which we will Email upon request)
• MUST have originality to the site.
• custom "contact us form" or request an estimate form.
Nice to have
• page for real customer testimonies.
• page for our previous work where we can upload pics of completed jobs.
Should not have
• any infringements on any copyrights or plagiarism at all.

```html
<!DOCTYPE html>
<html lang="en">
<head>
<meta charset="utf-8">
<title>Bright Lane Fixers – Home Repairs and Maintenance</title>
<link rel="stylesheet" href="https://fonts.googleapis.com/css2?family=Hind:wght@400;500;600;700&family=Roboto:wght@400;500&family=Saira+Semi+Condensed:wght@500&display=swap">
<style>
:root{
  --red:#e21e25;
  --ink:#222;
  --grey-text:#8a8a8a;
  --title-grey:#5f5f5f;
  --band-grey:#7f7f80;
  --stage:#efefef;
  --white:#fff;
}
*{box-sizing:border-box;margin:0;padding:0}
html,body{width:1200px;height:1200px;overflow:hidden;background:var(--stage);font-family:"Hind",sans-serif}
.page{position:absolute;left:105px;top:14px;width:990px;height:1173px;background:var(--white);box-shadow:0 6px 24px rgba(0,0,0,.25);overflow:hidden}
.topbar{position:absolute;left:0;top:0;width:100%;height:43px;background:var(--red);color:var(--white);font-size:12px;font-weight:500}
.topbar .call{position:absolute;left:37px;top:15px}
.social{position:absolute;display:flex;gap:12px}
.social span{width:15px;height:15px;border-radius:50%;background:var(--white)}
.topbar .social{left:733px;top:15px}
.topbar .search{position:absolute;left:883px;top:15px;display:flex;align-items:center;gap:14px}
.header{position:absolute;top:43px;left:0;width:100%;height:120px}
.brand{position:absolute;left:40px;top:66px;display:flex;align-items:center;gap:8px}
.brand .mark{width:14px;height:14px;background:var(--red)}
.brand .name{font-weight:700;font-size:14px;color:var(--ink);line-height:1}
.brand .sub{position:absolute;left:77px;top:20px;font-size:10px;font-weight:600;color:#444;white-space:nowrap}
.nav{position:absolute;right:82px;top:64px;display:flex;gap:15px;font-size:13px;color:#444;font-weight:500}
.nav .active{color:var(--red)}
.hero{position:absolute;top:163px;left:0;width:100%;height:394px;background:linear-gradient(160deg,#5d7a3e 0%,#8a9a6a 25%,#8f7c72 45%,#b58d7d 65%,#7c6a5e 100%)}
.quote-form{position:absolute;left:735px;top:21px;width:190px}
.field{height:27px;margin-bottom:8px;background:var(--white);border-radius:3px;border:1px solid #ccc;font-size:12px;color:#aaa;padding:5px 6px}
.field.message{height:105px;margin-bottom:9px}
.btn{height:28px;background:var(--red);color:var(--white);text-align:center;font-size:14px;font-weight:500;line-height:30px;border:1px solid #fff}
.hero-band{position:absolute;left:0;top:280px;width:100%;height:114px;background:rgba(40,40,40,.6);color:var(--white);text-align:center}
.hero-band p{font-size:16px;font-weight:500;line-height:20px}
.hero-band .lead{padding-top:13px}
.hero-band h1{font-family:"Saira Semi Condensed",sans-serif;font-weight:500;font-size:33px;margin-top:11px;letter-spacing:.3px}
.tagline{position:absolute;top:601px;width:100%;text-align:center;color:var(--red);font-family:"Roboto",sans-serif;font-size:20px;line-height:25px}
.band{position:absolute;top:686px;width:100%;height:26px;background:var(--band-grey);color:var(--white);text-align:center;font-family:"Roboto",sans-serif;font-size:23px;line-height:25px}
.service{position:absolute;width:250px;padding-left:42px}
.service .icon{position:absolute;left:0;top:0;width:28px;height:28px;border:3px solid #888;border-radius:3px}
.service h2{font-family:"Roboto",sans-serif;font-weight:500;font-size:14px;letter-spacing:1.3px;color:var(--title-grey);margin-bottom:3px}
.service p{font-size:11px;line-height:13.8px;color:var(--grey-text)}
.service a{font-size:11px;color:var(--red);text-decoration:none;display:block;margin-top:1px}
.footer{position:absolute;top:1084px;width:100%;height:89px;background:var(--red);color:var(--white)}
.footer nav{position:absolute;top:24px;left:0;width:100%;display:flex;justify-content:center;gap:0;font-size:12.5px;font-weight:600}
.footer nav a{color:var(--white);text-decoration:none;margin:0 17px}
.footer .social{left:444px;top:59px;gap:27px}
</style>
</head>
<body>
<div class="page">
  <div class="topbar">
    <span class="call">Call Today : 555-013-4827</span>
    <div class="social" aria-label="Social links"><span></span><span></span><span></span></div>
    <div class="search">Search
      <svg width="22" height="22" viewBox="0 0 22 22" fill="none" stroke="#fff" stroke-width="2"><circle cx="13" cy="9" r="6.5"/><line x1="8" y1="14" x2="2" y2="20"/></svg>
    </div>
  </div>

  <header class="header">
    <div class="brand"><span class="mark"></span><span class="name">Bright Lane Fixers</span></div>
    <span class="brand sub" style="position:absolute;left:78px;top:86px">And Maintenance</span>
    <nav class="nav"><span class="active">HOME</span><span>ABOUT</span><span>SERVICES</span><span>BLOG</span><span>CONTACT</span></nav>
  </header>

  <section class="hero" role="img" aria-label="Photo of a brick two-storey house with a shingle roof among trees">
    <form class="quote-form">
      <div class="field">Name :</div>
      <div class="field">Email :</div>
      <div class="field">Phone :</div>
      <div class="field message">Your message :</div>
      <div class="btn">GET QUOTE</div>
    </form>
    <div class="hero-band">
      <p class="lead">Looking for someone to help get your listing ready to show?</p>
      <p>A complete Home Repair Solution? Did an inspection reveal repairs needed before closing?</p>
      <h1>BRIGHT LANE FIXERS CAN HELP!</h1>
    </div>
  </section>

  <p class="tagline">One Name, One number, One call means one service for fast timely quotes,<br>home repairs and updates for you and/or your clients.</p>

  <div class="band">Home Repair Services</div>

  <article class="service" style="left:48px;top:779px">
    <span class="icon"></span>
    <h2>CARPENTRY</h2>
    <p>Stairs, Floors, Decks, Fences Storage sheds, Storage shelving and doors Vapor barrier repair/installation, Attic and crawl space</p>
    <a href="#">Read more →</a>
  </article>
  <article class="service" style="left:342px;top:779px">
    <span class="icon"></span>
    <h2>Doors &amp; Windows</h2>
    <p>Weatherstripping, Replacements Glass and Screen Installation and Repair, Install locksets</p>
    <a href="#">Read more →</a>
  </article>
  <article class="service" style="left:641px;top:779px">
    <span class="icon"></span>
    <h2>SMALL CONSTRUCTION</h2>
    <p>Stairs, Floors, Decks, Fences Storage sheds, Storage shelves Masonry</p>
    <a href="#">Read more →</a>
  </article>
  <article class="service" style="left:50px;top:888px">
    <span class="icon"></span>
    <h2>PLUMBING</h2>
    <p>Bathrooms, Kitchens, Washer/Dryer Hook Up Clogged drains, Toilets, Tubs/Showers Sinks, Garbage disposals, Leaking faucets vent repair</p>
    <a href="#">Read more →</a>
  </article>
  <article class="service" style="left:342px;top:888px">
    <span class="icon"></span>
    <h2>ROOFING MAINTENANCE</h2>
    <p>Painting, Pressure/Power washing Heavy lifting, Property Clean Outs Minor Repairs Vinyl Siding, Gutters, Clean and seal tile, Caulking, Patch and repair drywall, replace hard to reach light bulbs, Painting, Cosmetic repair, Debris removal.</p>
    <a href="#">Read more →</a>
  </article>
  <article class="service" style="left:635px;top:888px">
    <span class="icon"></span>
    <h2>ELECTRICAL</h2>
    <p>Bright Lane Fixers has licensed electricians who can rewire your entire house, or just a GFCI. We can respond to your electrical needs quickly. Code/Service Upgrades Fuses and Circuit Breakers Recessed Lighting Ceiling Fixtures You Name It!</p>
    <a href="#">Read more →</a>
  </article>

  <footer class="footer">
    <nav><a href="#">Home</a><a href="#">About</a><a href="#">Services</a><a href="#">Contact</a></nav>
    <div class="social" aria-label="Social links"><span></span><span></span><span></span></div>
  </footer>
</div>
</body>
</html>
```